Website Design - Financial Services Software

We are looking for website designs for our public website.
Some competitor sites we like are
www.ledgerwick.com.au
www.pluvo.com.au
www.plannerbeam.com
www.quorvia.com.au

A wireframe example of our site can be found at
http://tmw4rp.draftpane.com/

Attached is our logo.

Industry/Entity Type

Financial

```html
<!DOCTYPE html>
<html lang="en">
<head>
<meta charset="utf-8">
<title>Aurevia — Smarter Financial Strategies</title>
<link href="https://fonts.googleapis.com/css2?family=Marcellus&family=Fauna+One&display=swap" rel="stylesheet">
<style>
:root{
  --page:#eff0f2;
  --card:#ffffff;
  --border:#dcdde0;
  --gold:#c69a34;
  --gold-band:#c69a34;
  --ink:#2c2c2c;
  --muted:#555555;
  --footer:#282526;
  --footer-bar:#050505;
  --link-blue:#1a75b5;
  --chirp-blue:#4f8fd1;
  --button:#2e8fd6;
  --button-dark:#1f74b8;
  --white:#ffffff;
}
*{box-sizing:border-box;margin:0;padding:0}
html,body{width:1200px;height:1038px;overflow:hidden;background:var(--page)}
body{position:relative;font-family:"Fauna One",Georgia,serif;color:var(--ink)}
.card{position:absolute;left:93px;width:1018px;background:var(--card);border:1px solid var(--border);border-radius:10px;overflow:hidden}
.abs{position:absolute}

/* header */
.site-header{top:-10px;height:186px}
.brand{left:52px;top:33px;display:flex;align-items:center;gap:10px}
.brand-mark{width:26px;height:26px;background:var(--gold)}
.brand-name{font-family:"Marcellus",serif;font-size:38px;letter-spacing:2px;color:var(--gold);line-height:1}
.brand-tag{left:52px;top:82px;font-family:"Marcellus",serif;font-size:11px;letter-spacing:1px;color:var(--muted)}
.top-links{right:52px;top:36px;display:flex;align-items:center;gap:10px;font-family:"Marcellus",serif;font-size:13px;letter-spacing:.5px}
.social-box{width:23px;height:23px;display:block}
.social-box.linkpost{background:var(--link-blue)}
.social-box.chirper{background:var(--chirp-blue)}
.top-links .divider{width:1px;height:16px;background:#c9c9c9;margin:0 4px}
.main-nav{right:52px;top:143px;display:flex;align-items:center;font-family:"Marcellus",serif;font-size:17px;letter-spacing:.5px;color:var(--ink)}
.main-nav span{padding:0 32px}
.main-nav span:last-child{padding-right:0}
.main-nav .sep{width:1px;height:18px;background:#c0c0c0;padding:0}

/* hero */
.hero{top:188px;height:302px}
.hero-title{left:50px;top:22px;width:400px;font-family:"Marcellus",serif;font-weight:400;font-size:36px;line-height:37px;color:var(--gold)}
.hero-lede{left:50px;top:100px;font-size:12.5px;color:var(--ink)}
.tour{width:198px;text-align:center}
.tour .photo{height:104px;border:1px solid #c9c9c9}
.tour .label{margin-top:8px;font-family:"Marcellus",serif;font-size:12px;letter-spacing:.5px}
.tour-one{left:52px;top:153px}
.tour-two{left:280px;top:153px}
.tour-one .photo{background:linear-gradient(135deg,#cfd2d4,#8a8d92 55%,#e4e5e6)}
.tour-two .photo{background:linear-gradient(180deg,#7f97b4 0%,#c7c9c4 50%,#e0a250 72%,#2b2a2a 100%)}
.video{left:501px;top:16px;width:465px;height:270px;background:linear-gradient(120deg,#b6c0c6,#e7ecee 45%,#a8b4b7);overflow:hidden}
.video-title{left:10px;top:10px;background:#373c42;color:#3fa6e6;font-family:Arial,Helvetica,sans-serif;font-weight:bold;font-size:14px;padding:4px 10px}
.video-from{left:58px;top:36px;background:#23272b;color:#fff;font-family:Arial,Helvetica,sans-serif;font-size:9px;padding:4px 8px}
.video-action{right:11px;width:36px;height:26px;background:#3b3d40;border-radius:4px;color:#fff;font-family:Arial,Helvetica,sans-serif;font-size:7px;font-weight:bold;text-align:center;padding-top:15px}
.video-bar{left:10px;bottom:10px;width:445px;height:26px}
.play{left:0;top:0;width:60px;height:36px;background:#222;border-radius:3px;top:-8px}
.track{left:78px;top:0;width:375px;height:24px;background:#2a2a2a;border-radius:3px}
.track-line{left:10px;top:9px;width:286px;height:7px;background:#3d3d3d;border:1px solid #777}
.track-fill{left:0;top:0;width:125px;height:100%;background:#3fa6e6}
.track-time{left:120px;top:-12px;background:#fff;color:#222;font-family:Arial,sans-serif;font-size:8px;padding:1px 3px}
.track-hd{right:28px;top:5px;color:#3fa6e6;font-family:Arial,sans-serif;font-style:normal;font-weight:bold;font-size:10px}

/* about section */
.intro{top:500px;height:351px}
.intro-title{left:50px;top:26px;width:420px;font-family:"Marcellus",serif;font-weight:400;font-size:36px;line-height:37px;color:var(--gold)}
.intro-copy{left:50px;top:97px;width:425px;font-size:12.5px;line-height:19px}
.intro-copy p+p{margin-top:18px}
.gallery{left:509px;top:31px;display:grid;grid-template-columns:repeat(3,147px);grid-template-rows:repeat(2,97px);gap:8px 7px}
.gallery div{border:1px solid #c9c9c9}
.g1{background:linear-gradient(180deg,#3c4a2a,#6e8f3c 60%,#8c8f86)}
.g2{background:linear-gradient(135deg,#d8dde0,#a9c5de 60%,#e8e9ea)}
.g3{background:linear-gradient(135deg,#2a4a80,#8fb0d8 50%,#1e3766)}
.g4{background:linear-gradient(180deg,#1a1610,#b87a2e 45%,#f1c272 65%,#0b2942)}
.g5{background:linear-gradient(135deg,#3a2b22,#b5a49a 45%,#6d7b52)}
.g6{background:linear-gradient(180deg,#9fc4e6,#bcc9d1 55%,#576b6b)}
.signup-band{left:0;bottom:0;width:100%;height:88px;background:var(--gold-band)}
.signup-text{left:103px;top:31px;color:var(--white);font-size:19px}
.signup-button{left:654px;top:22px;width:204px;height:44px;background:linear-gradient(180deg,var(--button),var(--button-dark));border:1px solid #1b68a5;color:var(--white);font-family:"Marcellus",serif;font-size:17px;letter-spacing:.5px;display:flex;align-items:center;justify-content:center}

/* footer */
.site-footer{top:862px;height:200px;background:var(--footer);border:none}
.footer-brand{left:55px;top:40px;text-align:center;width:130px}
.footer-brand .brand-mark{width:22px;height:22px;background:var(--white);margin:0 auto 12px}
.footer-brand .brand-name{font-size:24px;color:var(--white);letter-spacing:1px}
.footer-brand .tag{margin-top:4px;font-family:"Marcellus",serif;font-size:8px;letter-spacing:1px;color:#d9d9d9}
.footer-col{top:28px;color:var(--white)}
.footer-col h3{font-family:"Marcellus",serif;font-weight:400;font-size:18px;margin-bottom:6px}
.footer-col li{list-style:none;font-size:12px;line-height:22px}
.footer-col li::before{content:"• "}
.col-about{left:270px}
.col-start{left:403px}
.col-legal{left:622px}
.col-connect{left:768px}
.connect-row{display:flex;align-items:center;gap:9px;font-family:"Marcellus",serif;font-size:12.5px;letter-spacing:.3px;margin-top:8px}
.connect-row:first-of-type{margin-top:4px}
.footer-bar{left:0;top:141px;width:100%;height:60px;background:var(--footer-bar)}
.copyright{left:55px;top:11px;color:var(--white);font-family:Arial,Helvetica,sans-serif;font-size:11px}
</style>
</head>
<body>

<header class="card site-header">
  <div class="abs brand"><span class="brand-mark"></span><span class="brand-name">AUREVIA</span></div>
  <div class="abs brand-tag">SMARTER FINANCIAL STRATEGIES</div>
  <div class="abs top-links">
    <span class="social-box linkpost" aria-label="Linkpost"></span>
    <span class="social-box chirper" aria-label="Chirper"></span>
    <span class="divider"></span>
    <span>LOGIN</span>
  </div>
  <nav class="abs main-nav">
    <span>FEATURES</span><i class="sep"></i>
    <span>EXAMPLES</span><i class="sep"></i>
    <span>FAQ</span><i class="sep"></i>
    <span>ABOUT</span>
  </nav>
</header>

<section class="card hero">
  <h1 class="abs hero-title">SMARTER FINANCIAL STRATEGIES</h1>
  <p class="abs hero-lede">Values and Cash-flow focused financial software for financial planners.</p>
  <div class="abs tour tour-one">
    <div class="photo" role="img" aria-label="Hands reviewing financial documents with a pen"></div>
    <div class="label">FEATURE TOUR</div>
  </div>
  <div class="abs tour tour-two">
    <div class="photo" role="img" aria-label="Silhouettes of business people shaking hands at sunset"></div>
    <div class="label">FEATURE TOUR</div>
  </div>
  <div class="abs video" role="img" aria-label="Video player showing a business meeting around a conference table">
    <div class="abs video-title">Smarter Financial Strategies</div>
    <div class="abs video-from">from Aurevia</div>
    <div class="abs video-action" style="top:12px">LIKE</div>
    <div class="abs video-action" style="top:44px">SHARE</div>
    <div class="abs video-action" style="top:76px">EMBED</div>
    <div class="abs video-bar">
      <div class="abs play">
        <svg width="60" height="36" viewBox="0 0 60 36"><path d="M25 12 L36 18 L25 24 Z" fill="#fff"/></svg>
      </div>
      <div class="abs track">
        <div class="abs track-line"><div class="abs track-fill"></div><span class="abs track-time">00:34</span></div>
        <span class="abs track-hd">HD</span>
        <svg class="abs" style="right:8px;top:7px" width="10" height="10" viewBox="0 0 10 10"><path d="M0 0h4L0 4zM10 0v4L6 0zM0 10V6l4 4zM10 10H6l4-4z" fill="#fff"/></svg>
      </div>
    </div>
  </div>
</section>

<section class="card intro">
  <h2 class="abs intro-title">LOREM IPSUM DOLOR SIT AMET</h2>
  <div class="abs intro-copy">
    <p>Lorem ipsum dolor sit amet, consectetur adipiscing elit. Morbi dapibus justo vel felis volutpat, sit amet congue arcu lacinia. Aenean elementum hendrerit turpis nec sodales.</p>
    <p>Maecenas vehicula justo et mauris tempus, vel dignissim dolor aliquet. Maecenas erat metus, scelerisque eget placerat gravida, consectetur fermentum magna</p>
  </div>
  <div class="abs gallery">
    <div class="g1" role="img" aria-label="Rocky garden landscape"></div>
    <div class="g2" role="img" aria-label="Two business men in conversation"></div>
    <div class="g3" role="img" aria-label="Glass office tower viewed from below"></div>
    <div class="g4" role="img" aria-label="Illuminated fountain in front of a hotel at night"></div>
    <div class="g5" role="img" aria-label="Stream flowing over stones"></div>
    <div class="g6" role="img" aria-label="City skyline across a river"></div>
  </div>
  <div class="abs signup-band">
    <p class="abs signup-text">Create an account today and begin your 30 day trial!</p>
    <div class="abs signup-button">SIGN UP NOW!</div>
  </div>
</section>

<footer class="card site-footer">
  <div class="abs footer-brand">
    <div class="brand-mark"></div>
    <div class="brand-name">AUREVIA</div>
    <div class="tag">SMARTER FINANCIAL STRATEGIES</div>
  </div>
  <div class="abs footer-col col-about"><h3>ABOUT</h3><ul><li>About Us</li><li>Support</li></ul></div>
  <div class="abs footer-col col-start"><h3>GETTING STARTED</h3><ul><li>Why Aurevia</li><li>Download a Summary</li><li>Aurevia Videos</li></ul></div>
  <div class="abs footer-col col-legal"><h3>LEGAL</h3><ul><li>Terms of Use</li><li>Privacy</li></ul></div>
  <div class="abs footer-col col-connect"><h3>CONNECT</h3>
    <div class="connect-row"><span class="social-box linkpost"></span>AUREVIA ON LINKPOST</div>
    <div class="connect-row"><span class="social-box chirper"></span>AUREVIA ON CHIRPER</div>
  </div>
  <div class="abs footer-bar"><p class="abs copyright">Copyright © 2014 Aurevia Pty Ltd. All rights reserved.</p></div>
</footer>

</body>
</html>
```